Letterhead and Business card for Construction company

We need a letterhead and business card with our new company logo. We are based in NY. We develop and build properties.

The design should incorporate some unique feature from the logo (shape, font...). it should look like an extension from it.

Design should be clean and elegant, professional, not too busy.

The letterhead should include:
Logo (attached)
Address
Phone
Email

Please find the attached logo images and AI file.

Target Market(s)

Construction industry professionals

Industry/Entity Type

Construction, Development

Font styles to use
Sans Serif

Colors

Designer to choose colors to be used in the design.

Requirements
Must have
• Design should incorporate logo elements, additional assets are welcome. I'd like to see some other shapes / images invorporated too.

```html
<!DOCTYPE html>
<html lang="en">
<head>
<meta charset="utf-8">
<title>Meridian Build – Letterhead and Business Cards</title>
<link href="https://fonts.googleapis.com/css2?family=Open+Sans:wght@400;600;800&family=Michroma&display=swap" rel="stylesheet">
<style>
  :root {
    --orange: #f37b20;
    --charcoal: #323232;
    --charcoal-deep: #262626;
    --ink: #3a3a3a;
    --paper: #ffffff;
    --backdrop-edge: #a9a9a9;
    --backdrop-mid: #e2e2e2;
  }
  * { box-sizing: border-box; margin: 0; padding: 0; }
  html, body { width: 1200px; height: 1200px; overflow: hidden; }
  body {
    position: relative;
    background: linear-gradient(90deg, var(--backdrop-edge) 0%, var(--backdrop-mid) 50%, var(--backdrop-edge) 100%);
    font-family: "Open Sans", sans-serif;
    color: var(--ink);
  }

  /* Wordmark */
  .wordmark {
    position: absolute;
    display: flex;
    align-items: center;
    gap: 8px;
    font-family: "Open Sans", sans-serif;
    font-weight: 800;
    line-height: 0.95;
    letter-spacing: 0.02em;
    color: var(--charcoal);
  }
  .wordmark .mark-square { width: 16px; height: 16px; background: var(--orange); flex: none; }
  .wordmark .mark-text { display: block; }

  /* Letterhead */
  .letterhead {
    position: absolute;
    left: 60px; top: 129px;
    width: 665px; height: 940px;
    background: var(--paper);
  }
  .letterhead .wordmark { left: 62px; top: 36px; font-size: 28px; }
  .letterhead-contact {
    position: absolute;
    left: 473px; top: 56px;
    padding-left: 10px;
    border-left: 1px solid var(--orange);
    font-family: "Michroma", sans-serif;
    font-size: 8px;
    line-height: 10.6px;
    color: var(--charcoal);
  }
  .contact-address { margin-bottom: 6px; }
  .contact-label { color: var(--orange); display: inline-block; width: 15px; }
  .accent { color: var(--orange); }

  .recipient {
    position: absolute;
    left: 62px; top: 193px;
    font-size: 11.5px;
    line-height: 16.2px;
  }
  .salutation {
    position: absolute;
    left: 62px; top: 310px;
    font-size: 11.5px;
  }
  .letter-body {
    position: absolute;
    left: 62px; top: 349px;
    width: 542px;
    font-size: 11.8px;
    line-height: 20.1px;
    text-align: justify;
  }
  .closing {
    position: absolute;
    left: 62px; top: 624px;
    font-size: 11.5px;
  }
  .signature-area {
    position: absolute;
    left: 62px; top: 660px;
    width: 224px; height: 72px;
    background: linear-gradient(90deg, #f1f1f1, #fafafa);
  }
  .letterhead-band {
    position: absolute;
    left: 0; bottom: 0;
    width: 100%; height: 10px;
    background: var(--orange);
  }

  /* Business card front */
  .card {
    position: absolute;
    left: 757px;
    width: 399px; height: 238px;
    overflow: hidden;
  }
  .card-front { top: 355px; background: var(--paper); }
  .card-front .wordmark { left: 54px; top: 100px; font-size: 20px; }
  .card-front .wordmark .mark-square { width: 12px; height: 12px; }
  .card-details {
    position: absolute;
    left: 202px; top: 76px;
    height: 92px;
    padding-left: 12px;
    border-left: 1px solid var(--charcoal);
    font-family: "Michroma", sans-serif;
    font-size: 7px;
    line-height: 9.4px;
    color: var(--charcoal);
  }
  .card-name {
    font-family: "Open Sans", sans-serif;
    font-weight: 600;
    font-size: 12.5px;
    line-height: 13px;
    color: var(--orange);
    letter-spacing: -0.01em;
  }
  .card-role {
    font-family: "Open Sans", sans-serif;
    font-weight: 600;
    font-size: 8px;
    line-height: 10px;
    margin-bottom: 9px;
  }
  .card-details .contact-address { margin-bottom: 7px; }
  .card-details .contact-label { width: 13px; }
  .card-band { position: absolute; left: 0; bottom: 0; width: 100%; height: 8px; }

  /* Business card back */
  .card-back {
    top: 619px;
    background: linear-gradient(90deg, #2b2b2b 0%, #383838 30%, #303030 55%, var(--charcoal) 100%);
  }
  .card-back .wordmark {
    left: 0; right: 0; top: 100px;
    justify-content: center;
    color: var(--paper);
    font-size: 26px;
  }
</style>
</head>
<body>

<section class="letterhead" aria-label="Letterhead">
  <div class="wordmark">
    <span class="mark-square"></span>
    <span class="mark-text">MERIDIAN<br>BUILD</span>
  </div>

  <address class="letterhead-contact" style="font-style:normal">
    <div class="contact-address">Main Street, Number 01/A<br>123456 City Name<br>State Country</div>
    <div><span class="contact-label">T:</span>+00 (212)555-0147</div>
    <div><span class="contact-label">E:</span>office@meridianbuild.com</div>
    <div><span class="contact-label">W:</span>www.<span class="accent">meridianbuild</span>.com</div>
  </address>

  <div class="recipient">
    Mr. Peter Lind<br>President<br>Northgate Advisors<br>111 Street Name,<br>City State, 12345
  </div>

  <p class="salutation">Dear :</p>

  <div class="letter-body">
    <p>Lorem ipsum dolor sit amet, consectetur adipiscing elit. Aenean ut ipsum eget massa hendrerit vestibulum vel in velit. Donec pretium neque velit.</p>
    <p>Aliquam porta lectus nec mauris ornare venenatis. Vivamus non est turpis, et cursus sem. Mauris vehicula erat in diam auctor at bibendum nisl lacinia.</p>
    <p>Morbi imperdiet neque vehicula nunc convallis gravida. Vestibulum iaculis pretium placerat. Integer consequat, est sit amet facilisis eleifend, nibh nibh varius orci, eget dapibus arcu dui non purus. Pellentesque in magna mauris. Duis enim sapien, dictum vitae condimentum a, pulvinar vel lacus. Mauris et molestie nibh. Vestibulum vitae nulla at metus elementum porta sit amet interdum elit. Nulla sollicitudin neque eu nulla volutpat congue.</p>
    <p>Etiam pellentesque, velit id dapibus fermentum, turpis sapien ornare dui, ac tincidunt ligula odio congue purus. Nunc sed ante dui, in porta lectus. Cras nec sem lorem. In hac habitasse platea dictumst. Maecenas id diam quis dui porta tristique. Sed id egestas felis. Donec ullamcorper mattis posuere. Phasellus fermentum eleifend tortor vel dapibus. Vestibulum ante ipsum.</p>
  </div>

  <p class="closing">Sincerely,</p>
  <div class="signature-area" role="img" aria-label="Handwritten signature of Marcus Vale"></div>

  <div class="letterhead-band"></div>
</section>

<section class="card card-front" aria-label="Business card front">
  <div class="wordmark">
    <span class="mark-square"></span>
    <span class="mark-text">MERIDIAN<br>BUILD</span>
  </div>
  <address class="card-details" style="font-style:normal">
    <div class="card-name">MARCUS VALE</div>
    <div class="card-role">Founder &amp; CEO</div>
    <div class="contact-address">Main Street, Number 01/A<br>123456 City Name<br>State Country</div>
    <div><span class="contact-label accent">T:</span>+00 (212)555-0147</div>
    <div><span class="contact-label accent">E:</span>office@meridianbuild.com</div>
    <div><span class="contact-label accent">W:</span>www.<span class="accent">meridianbuild</span>.com</div>
  </address>
  <svg class="card-band" viewBox="0 0 399 8" preserveAspectRatio="none" aria-hidden="true">
    <polygon points="0,0 206,0 198,8 0,8" fill="#323232"/>
    <polygon points="206,0 399,0 399,8 198,8" fill="#f37b20"/>
  </svg>
</section>

<section class="card card-back" aria-label="Business card back">
  <div class="wordmark">
    <span class="mark-square"></span>
    <span class="mark-text">MERIDIAN<br>BUILD</span>
  </div>
</section>

</body>
</html>
```